Wedding Marlies & Joost - Save the Date Wedding Card

I would like to have a creative save the date wedding card. We like grey/black/white colors and modern/ plain and simple.
I like the Save the Date copy big and book a flight copy smaller. I like stylish fonts for the save the date copy
Copy front:
Save the Date & book a flight
7-10-2017 Denia (Spanje)
Marlies & Joost
Onze dag is niet compleet zonder jou!
Copy back:
6-10 preferred travel date
7-10 wedding ceremony/drinks/dinner/party
8-10 hangover breakfast
Nearest Airports Valencia & Alicante
More info will be available soon!
wedding guests
Wedding

```html
<!DOCTYPE html>
<html lang="nl">
<head>
<meta charset="utf-8">
<title>Save the Date – Marlies &amp; Joost</title>
<link href="https://fonts.googleapis.com/css2?family=Didact+Gothic&family=Dancing+Script:wght@600;700&family=Caveat:wght@400&display=swap" rel="stylesheet">
<style>
  :root {
    --page: #ffffff;
    --card: #000000;
    --ink: #ffffff;
    --ornament: #bdbdbd;
    --ornament-soft: #8c8c8c;
  }
  * { margin: 0; padding: 0; box-sizing: border-box; }
  html, body { width: 1159px; height: 1200px; overflow: hidden; background: var(--page); }
  .canvas { position: relative; width: 1159px; height: 1200px; }

  .card {
    position: absolute;
    top: 413px;
    height: 373px;
    background: var(--card);
    color: var(--ink);
    font-family: "Didact Gothic", sans-serif;
    overflow: hidden;
  }
  .card--back { left: 22px; width: 546px; }
  .card--front { left: 585px; width: 526px; }

  .line { position: absolute; left: 0; right: 0; text-align: center; white-space: nowrap; line-height: 1; }

  .dotted { position: absolute; height: 3px;
    background-image: radial-gradient(circle, var(--ink) 1.2px, transparent 1.5px);
    background-size: 8px 3px; background-repeat: repeat-x; }

  .ornament { position: absolute; }

  /* back */
  .date { font-size: 19px; letter-spacing: 2px; }
  .event { font-size: 19px; font-style: italic; letter-spacing: 1.5px; }
  .airports { font-size: 15px; letter-spacing: 0.6px; }
  .note { font-size: 15px; font-weight: 700; letter-spacing: 0.6px; -webkit-text-stroke: 0.4px var(--ink); }
  .bullets { display: flex; justify-content: center; gap: 10px; }
  .bullets span { width: 8px; height: 8px; border-radius: 50%; background: var(--ink); }

  /* front */
  .headline { font-family: "Dancing Script", cursive; font-weight: 700; font-size: 52px; }
  .joiner { font-size: 15px; letter-spacing: 1px; }
  .subline { font-family: "Dancing Script", cursive; font-weight: 700; font-size: 31px; }
  .tagline { font-family: "Caveat", cursive; font-size: 24px; letter-spacing: 0.5px; }
  .details { font-size: 17px; letter-spacing: 1.2px; }
</style>
</head>
<body>
<main class="canvas">

  <section class="card card--back" aria-label="Achterkant: programma">
    <div class="dotted" style="left:16px; width:138px; top:45px;"></div>
    <div class="dotted" style="left:400px; width:132px; top:45px;"></div>
    <svg class="ornament" style="left:150px; top:26px;" width="246" height="44" role="img" aria-label="Barok bladornament bovenaan">
      <rect x="0" y="0" width="246" height="44" rx="20" fill="var(--ornament)" opacity="0.85"/>
    </svg>

    <p class="line date" style="top:75px;">6 · 10</p>
    <p class="line event" style="top:97px;">preferred travel date</p>
    <p class="line date" style="top:130px;">7 · 10</p>
    <p class="line event" style="top:153px;">wedding ceremony / drinks / dinner / party</p>
    <p class="line date" style="top:185px;">8 · 10</p>
    <p class="line event" style="top:209px;">hangover breakfast</p>
    <div class="line bullets" style="top:239px;"><span></span><span></span><span></span></div>
    <p class="line airports" style="top:260px;">Nearest Airports Valencia &amp; Alicante</p>
    <p class="line note" style="top:280px;">More info will be available soon!</p>

    <div class="dotted" style="left:16px; width:150px; top:319px;"></div>
    <div class="dotted" style="left:390px; width:142px; top:319px;"></div>
    <svg class="ornament" style="left:165px; top:300px;" width="216" height="40" role="img" aria-label="Barok bladornament onderaan">
      <rect x="0" y="0" width="216" height="40" rx="18" fill="var(--ornament)" opacity="0.85"/>
    </svg>
  </section>

  <section class="card card--front" aria-label="Voorkant: save the date">
    <svg class="ornament" style="left:100px; top:27px;" width="326" height="46" role="img" aria-label="Barok bladornament, bovenkant van het kader">
      <rect x="0" y="0" width="326" height="46" rx="22" fill="var(--ornament)" opacity="0.85"/>
    </svg>
    <svg class="ornament" style="left:82px; top:80px;" width="34" height="150" role="img" aria-label="Krulornament, linkerkant van het kader">
      <rect x="0" y="0" width="34" height="150" rx="17" fill="var(--ornament-soft)"/>
    </svg>
    <svg class="ornament" style="left:420px; top:80px;" width="34" height="150" role="img" aria-label="Krulornament, rechterkant van het kader">
      <rect x="0" y="0" width="34" height="150" rx="17" fill="var(--ornament-soft)"/>
    </svg>
    <svg class="ornament" style="left:110px; top:238px;" width="306" height="44" role="img" aria-label="Barok bladornament, onderkant van het kader">
      <rect x="0" y="0" width="306" height="44" rx="20" fill="var(--ornament)" opacity="0.85"/>
    </svg>

    <h1 class="line headline" style="top:96px;">Save the Date</h1>
    <div class="dotted" style="left:152px; width:80px; top:168px;"></div>
    <p class="line joiner" style="top:161px;">AND</p>
    <div class="dotted" style="left:290px; width:80px; top:168px;"></div>
    <h2 class="line subline" style="top:188px;">Book a flight</h2>

    <p class="line tagline" style="top:299px;">Onze dag is niet compleet zonder jou!</p>
    <p class="line details" style="top:336px;">7 ·10 · 2017 • Denia (Spanje) • Marlies &amp; Joost</p>
  </section>

</main>
</body>
</html>
```